Northgate Baptist Church Banner Design

Designing 6 banners (3 + 3 that will hang on opposite sides of our auditorium) that are 10 feet long by 4 feet wide.

Use our branding guide - specifically item 4 (vertical logo) and item 5 (icon logo).

Design elements found in our ASCEND booklet, we would like to see designs that utilize the white, green and blue colour palettes but NOT the grey. Other colours may be incorporated (e.g. coral).

We are looking for 3 banner designs that would match on either side of the auditorium, the first banner incorporating the word "TRUTH", the second incorporating the word "LOVE", and the third incorporating the word "MISSION".

We interested in incorporating graphics such as trees or outdoor themes.

Font styles to use
Other font styles liked:
• Montserrat

Colors
34a7d7
00a990
f47c35

Requirements
Must have
• Banner Type #1 include the word "TRUTH"
Banner Type #2 include the word "LOVE"
Banner Type #3 include the word "MISSION"

Colour scheme must include CMYK 54 / 5 / 16 / 0 (which is available in the branding guide.) We have selected the three colours, included below in the brief.

From the branding guide - utilize #5 (icon) for the banner.

UPDATE: After reviewing the initial submissions, we are asking for designs that ONLY incorporate #5 - the ICON logo for the banners.
Nice to have
• It would be nice to have some creativity with the colour ... though a more minimalistic style is preferred.

Graphic adaptations such as trees in the background would be of interest.
Should not have
• Colour scheme should not be gray scale.

The banners should NOT be too busy.

Scripture verses (written out) are not necessary.

```html
<!DOCTYPE html>
<html lang="en">
<head>
<meta charset="utf-8">
<title>Northgate Baptist Church – Auditorium Banners</title>
<link href="https://fonts.googleapis.com/css2?family=Montserrat:wght@700;800&family=Permanent+Marker&display=swap" rel="stylesheet">
<style>
  :root{
    --truth:#67c3d1;
    --love:#66c28c;
    --mission:#2ea6da;
    --white:#ffffff;
    --sky:#dfe3e8;
    --cloud:#b9c2cc;
    --rock:#3e4c5c;
    --forest:#1f3329;
    --lake:#2aa3a8;
    --lake-deep:#1f8e95;
    --brand:#4aaebb;
  }
  *{margin:0;padding:0;box-sizing:border-box}
  html,body{width:1200px;height:2349px;overflow:hidden;background:var(--white)}
  .canvas{position:relative;width:1200px;height:2349px;background:var(--white)}
  .banner{position:absolute;width:300px;overflow:hidden}
  .scene{position:absolute;inset:0;
    background:linear-gradient(180deg,var(--sky) 0%,var(--cloud) 12%,var(--rock) 30%,var(--rock) 55%,var(--forest) 68%,var(--lake) 72%,var(--lake-deep) 100%)}
  .scene.soft{filter:blur(3px);transform:scale(1.05)}
  .scene.low{background:linear-gradient(180deg,var(--sky) 0%,var(--cloud) 10%,var(--rock) 26%,var(--rock) 52%,var(--forest) 66%,var(--lake) 75%,var(--lake-deep) 100%)}
  .word-bar{position:absolute;display:flex;flex-direction:column;align-items:center;justify-content:center;color:var(--white)}
  .word-bar.script{font-family:"Permanent Marker","Montserrat",cursive;font-size:76px;line-height:78px;font-style:italic}
  .word-bar.sans{font-family:"Montserrat",sans-serif;font-weight:700;font-size:60px;line-height:71px}
  .word-band{position:absolute;left:0;bottom:0;width:300px;height:127px;display:flex;align-items:center;justify-content:center;
    font-family:"Montserrat",sans-serif;font-weight:800;font-size:50px;letter-spacing:3px;color:var(--white)}
  .truth{background:var(--truth)} .love{background:var(--love)} .mission{background:var(--mission)}
  .badge{position:absolute;width:98px;height:98px;border-radius:50%;background:var(--white);
    display:flex;align-items:center;justify-content:center;padding:0 14px;
    font-family:"Montserrat",sans-serif;font-weight:700;font-size:12px;line-height:14px;
    color:var(--brand);text-align:center}
</style>
</head>
<body>
<main class="canvas">

  <section class="banner" style="left:0;top:0;height:750px">
    <div class="scene soft" role="img" aria-label="Blurred photo of a turquoise mountain lake with rocky peaks"></div>
    <div class="word-bar script truth" style="left:0;top:308px;width:128px;height:442px"><span>T</span><span>R</span><span>U</span><span>T</span><span>H</span></div>
    <div class="badge" style="left:182px;top:19px">Northgate Baptist Church</div>
  </section>

  <section class="banner" style="left:449px;top:0;height:750px">
    <div class="scene soft" role="img" aria-label="Blurred photo of a mountain valley with snow and pine trees above a lake"></div>
    <div class="word-bar script love" style="left:124px;top:0;width:127px;height:361px"><span>L</span><span>O</span><span>V</span><span>E</span></div>
    <div class="badge" style="left:19px;top:632px">Northgate Baptist Church</div>
  </section>

  <section class="banner" style="left:900px;top:0;height:750px">
    <div class="scene soft" role="img" aria-label="Blurred photo of forested lakeshore under mountain peaks"></div>
    <div class="word-bar script mission" style="left:133px;top:155px;width:128px;height:595px"><span>M</span><span>I</span><span>S</span><span>S</span><span>I</span><span>O</span><span>N</span></div>
    <div class="badge" style="left:20px;top:19px">Northgate Baptist Church</div>
  </section>

  <section class="banner" style="left:0;top:800px;height:748px">
    <div class="scene" role="img" aria-label="Photo of mountain cliffs over a turquoise lake with canoes"></div>
    <div class="word-bar sans truth" style="left:0;top:316px;width:128px;height:432px"><span>T</span><span>R</span><span>U</span><span>T</span><span>H</span></div>
    <div class="badge" style="left:182px;top:17px">Northgate Baptist Church</div>
  </section>

  <section class="banner" style="left:449px;top:800px;height:748px">
    <div class="scene" role="img" aria-label="Photo of a snowy mountain gully with pine trees by a lake"></div>
    <div class="word-bar sans love" style="left:0;top:387px;width:127px;height:361px"><span>L</span><span>O</span><span>V</span><span>E</span></div>
    <div class="badge" style="left:181px;top:17px">Northgate Baptist Church</div>
  </section>

  <section class="banner" style="left:900px;top:800px;height:748px">
    <div class="scene low" role="img" aria-label="Photo of pine forest on a lakeshore below mountain peaks"></div>
    <div class="word-bar sans mission" style="left:0;top:175px;width:128px;height:573px"><span>M</span><span>I</span><span>S</span><span>S</span><span>I</span><span>O</span><span>N</span></div>
    <div class="badge" style="left:182px;top:17px">Northgate Baptist Church</div>
  </section>

  <section class="banner" style="left:0;top:1599px;height:750px">
    <div class="scene" role="img" aria-label="Photo of mountain cliffs above a turquoise lake with canoes"></div>
    <div class="word-band truth">TRUTH</div>
    <div class="badge" style="left:182px;top:18px">Northgate Baptist Church</div>
  </section>

  <section class="banner" style="left:449px;top:1599px;height:750px">
    <div class="scene" role="img" aria-label="Photo of snowy mountain peaks and pine trees above a lake"></div>
    <div class="word-band love">LOVE</div>
    <div class="badge" style="left:181px;top:18px">Northgate Baptist Church</div>
  </section>

  <section class="banner" style="left:900px;top:1599px;height:750px">
    <div class="scene low" role="img" aria-label="Photo of dense pine forest on a lakeshore under cloudy peaks"></div>
    <div class="word-band mission">MISSION</div>
    <div class="badge" style="left:182px;top:18px">Northgate Baptist Church</div>
  </section>

</main>
</body>
</html>
```